Dune crest Website

We need a simple web page design for our businessWe procure and dispose of earthmoving construction equipmentwe also find construction equipment for our customers using our global contacts

Number of Pages Required

1 page

```html
<!DOCTYPE html>
<html lang="en">
<head>
<meta charset="utf-8">
<title>Dune crest – Earthmoving Construction Equipment</title>
<link rel="stylesheet" href="https://fonts.googleapis.com/css2?family=Montserrat:wght@400;500;600;700&family=Barlow+Condensed:wght@500;600&display=swap">
<style>
:root{
  --orange:#f8b12e;
  --orange-deep:#e9a21f;
  --ink:#1d1d1d;
  --text:#555;
  --dark:#2a2a2a;
  --darker:#1e1e1e;
  --white:#fff;
}
*{margin:0;padding:0;box-sizing:border-box}
html,body{width:1200px;height:2853px;overflow:hidden;background:var(--white)}
body{position:relative;font-family:"Montserrat",sans-serif;color:var(--ink)}
.abs{position:absolute}
.label{font-family:"Barlow Condensed",sans-serif;font-weight:600;text-transform:uppercase;letter-spacing:.3px}

/* header */
.site-header{left:0;top:0;width:1200px;height:91px;background:var(--orange)}
.brand-name{left:46px;top:16px;font-family:"Montserrat",sans-serif;font-weight:500;font-size:38px;letter-spacing:2px;color:var(--ink);line-height:1}
.brand-tag{left:78px;top:57px;font-family:"Barlow Condensed",sans-serif;font-weight:600;font-size:15px;color:var(--ink)}
.main-nav a{position:absolute;top:37px;font-size:16px;color:#3b3b3b;text-decoration:none}
.main-nav a.current{color:var(--ink);border-bottom:2px solid var(--ink)}
.header-contact .icon{left:940px;top:24px}
.phone-number{left:1014px;top:22px;font-family:"Barlow Condensed",sans-serif;font-weight:600;font-size:24px;color:var(--ink)}
.email{left:1014px;top:50px;font-family:"Barlow Condensed",sans-serif;font-weight:500;font-size:16px;color:#3b3b3b}

/* hero */
.hero{left:0;top:91px;width:1200px;height:556px;background:linear-gradient(180deg,#4a5666 0%,#8a6a48 38%,#c98a3a 55%,#5b4a36 78%,#3a3128 100%)}
.hero h1{left:0;top:176px;width:1200px;text-align:center;font-size:42px;font-weight:700;color:var(--white);line-height:46px}
.btn{display:block;background:var(--orange);color:var(--ink);font-family:"Barlow Condensed",sans-serif;font-weight:600;text-transform:uppercase;text-align:center;text-decoration:none}
.hero .btn{position:absolute;left:527px;top:300px;width:144px;height:32px;line-height:32px;font-size:15px}
.hero-bar{left:0;top:482px;width:1200px;height:74px;background:rgba(20,20,20,.72)}
.hero-bar .item{position:absolute;top:0;height:74px;display:flex;align-items:center;gap:14px;color:var(--white);font-family:"Barlow Condensed",sans-serif;font-weight:600;font-size:22px;text-transform:uppercase}
.hero-bar .divider{position:absolute;left:601px;top:18px;width:1px;height:38px;background:rgba(255,255,255,.35)}

/* intro */
.section-title{left:0;width:1200px;text-align:center;font-size:34px;font-weight:600;line-height:44px;color:var(--ink)}
.rule{height:3px;width:92px;background:linear-gradient(90deg,var(--ink) 50%,var(--orange) 50%)}
.intro-lead{left:0;top:848px;width:1200px;text-align:center;font-size:23px;color:#555}
.intro-lead b{font-weight:600;color:var(--ink)}
.intro-lead span{color:var(--orange);font-weight:600}
.intro-small{left:0;top:882px;width:1200px;text-align:center;font-size:17px;color:#666}

.equipment-grid{left:48px;top:945px;width:1107px;height:369px;display:flex}
.equipment-card{position:relative;flex:1;height:100%}
.equipment-card .name{position:absolute;left:0;width:100%;text-align:center;color:var(--white);font-family:"Barlow Condensed",sans-serif;font-weight:600;font-size:23px;line-height:26px;text-transform:uppercase}
.arrow-icon{position:absolute}

/* about */
.about-title{left:93px;top:1444px;width:443px;text-align:center;font-size:34px;font-weight:600}
.about-title span{color:var(--orange)}
.about-sub{left:93px;top:1489px;width:443px;text-align:center;font-size:17px;color:#555}
.about-text{left:93px;width:443px;font-size:13.5px;line-height:21px;color:#555;text-align:justify;letter-spacing:.3px}
.about .btn{position:absolute;left:240px;top:1784px;width:148px;height:38px;line-height:38px;font-size:16px;text-transform:none}
.about-photo{left:618px;top:1407px;width:582px;height:461px;background:linear-gradient(160deg,#dcdfe4 0%,#b9b2a6 30%,#7b6f62 60%,#4b4640 100%)}

/* industries */
.industry-strip{left:0;top:2022px;width:1200px;height:239px;display:flex}
.industry-tile{position:relative;flex:1;height:100%}
.industry-tile .name{position:absolute;left:0;width:100%;text-align:center;color:var(--white);font-family:"Barlow Condensed",sans-serif;font-weight:600;font-size:23px;line-height:26px;text-transform:uppercase}

.cta-bar{left:0;top:2261px;width:1200px;height:75px;background:var(--orange)}
.cta-bar .item{position:absolute;top:0;height:75px;display:flex;align-items:center;gap:14px;font-family:"Barlow Condensed",sans-serif;font-weight:600;font-size:17px;text-transform:uppercase;color:var(--ink)}
.cta-bar .divider{position:absolute;top:21px;width:1px;height:34px;background:rgba(0,0,0,.25)}

/* testimonial */
.testimonial{left:0;top:2336px;width:1200px;height:367px;background:linear-gradient(180deg,#3c3c3c 0%,#2c2c2c 60%,#242424 100%)}
.testimonial blockquote{position:absolute;left:300px;top:162px;width:600px;text-align:center;color:var(--white);font-size:14px;line-height:23px}
.testimonial cite{position:absolute;left:0;top:298px;width:1200px;text-align:center;font-style:normal;color:var(--white);font-family:"Barlow Condensed",sans-serif;font-weight:600;font-size:15px;letter-spacing:1px}

.social-bar{left:0;top:2703px;width:1200px;height:76px;background:var(--orange)}
.social-bar .dot{position:absolute;top:31px;width:14px;height:14px;border:2px solid #444;border-radius:3px}

.site-footer{left:0;top:2779px;width:1200px;height:74px;background:var(--darker)}
.copyright{left:44px;top:28px;font-size:12px;color:#ccc}
.copyright span{color:var(--orange)}
.footer-nav a{position:absolute;top:28px;font-size:13px;color:#ddd;text-decoration:none}
.footer-nav a.current{color:var(--orange)}
.back-top{left:1086px;top:28px;font-size:13px;color:#ddd;display:flex;gap:8px;align-items:center}
</style>
</head>
<body>

<header class="site-header abs">
  <div class="brand-name abs">DUNECREST</div>
  <div class="brand-tag abs">Earthmoving Construction Equipment</div>
  <nav class="main-nav label">
    <a class="current" href="#" style="left:415px">Company</a>
    <a href="#" style="left:510px">Equipment</a>
    <a href="#" style="left:614px">Industry</a>
    <a href="#" style="left:711px">Services</a>
    <a href="#" style="left:806px">Contact</a>
  </nav>
  <div class="header-contact">
    <svg class="icon abs" width="42" height="42" viewBox="0 0 42 42"><circle cx="21" cy="21" r="21" fill="#1d1d1d"/><path d="M15 13c1-1 2-1 3 0l2 3c.5 1 0 2-1 2.5-.5.5 0 1.5 1 3s2.5 2.5 3 2c.5-1 1.5-1.5 2.5-1l3 2c1 1 1 2 0 3-2 2-5 1-9-3s-6.5-8-4.5-11.5z" fill="#f8b12e"/></svg>
    <div class="phone-number abs">0491 570 156</div>
    <div class="email abs">hello@dunecrest.com.au</div>
  </div>
</header>

<section class="hero abs" role="img" aria-label="Yellow backhoe loader on a rocky site against a sunset sky">
  <h1 class="abs">For all your<br>earth moving needs</h1>
  <a class="btn" href="#">Contact Us</a>
  <div class="hero-bar abs">
    <div class="item" style="left:214px">
      <svg width="32" height="32" viewBox="0 0 32 32"><circle cx="16" cy="16" r="16" fill="#f8b12e"/><path d="M10 22l1-4 8-8 3 3-8 8z" fill="#1d1d1d"/></svg>
      Request a price
    </div>
    <div class="divider"></div>
    <div class="item" style="left:777px">
      <svg width="32" height="32" viewBox="0 0 32 32"><circle cx="16" cy="16" r="16" fill="#f8b12e"/><path d="M11 9c.7-.7 1.5-.7 2 0l1.5 2.2c.4.7 0 1.4-.7 1.8-.4.4 0 1.1.7 2.2s1.8 1.8 2.2 1.5c.4-.7 1.1-1.1 1.8-.7l2.2 1.5c.7.7.7 1.5 0 2.2-1.5 1.5-3.7.7-6.6-2.2S9.5 11.5 11 9z" fill="#1d1d1d"/></svg>
      Call: 0491 570 156
    </div>
  </div>
</section>

<h2 class="section-title abs" style="top:729px">Earthmoving Equipment Supplier<br>Based in Australia</h2>
<div class="rule abs" style="left:555px;top:826px"></div>
<p class="intro-lead abs">If you’re looking for earthmoving equipment, visit <b>Dune</b> <span>crest</span> today!</p>
<p class="intro-small abs">we specialise in supplying a wide range of earthmoving equipment.</p>

<div class="equipment-grid abs">
  <div class="equipment-card" role="img" aria-label="Yellow backhoe loader under a blue sky" style="background:linear-gradient(180deg,#8fb3d6 0%,#c9d6df 40%,#b49a3a 60%,#555 100%)">
    <div class="name" style="top:266px">4x4 Backhoe<br>Loader</div>
  </div>
  <div class="equipment-card" role="img" aria-label="Yellow soil compactor roller on a dirt road" style="background:linear-gradient(180deg,#c9ccd0 0%,#9a9a96 35%,#6b6a5a 60%,#3f3d39 100%)">
    <div class="name" style="top:142px">Soil<br>Compactor</div>
    <svg class="arrow-icon" style="left:170px;top:274px" width="30" height="30" viewBox="0 0 30 30"><circle cx="15" cy="15" r="13" fill="none" stroke="#f8b12e" stroke-width="2"/><path d="M9 15h11M16 10l5 5-5 5" fill="none" stroke="#f8b12e" stroke-width="2"/></svg>
  </div>
  <div class="equipment-card" role="img" aria-label="Yellow tracked excavator on a quarry" style="background:linear-gradient(180deg,#7fa6cc 0%,#b9a98c 35%,#b0713e 65%,#7a4a2a 100%)">
    <div class="name" style="top:266px">Tracked<br>Excavators</div>
  </div>
</div>

<section class="about">
  <h2 class="about-title abs">Dune <span>crest</span></h2>
  <p class="about-sub abs">Earthmoving Construction Equipment</p>
  <div class="rule abs" style="left:268px;top:1523px"></div>
  <p class="about-text abs" style="top:1550px">With over 30 years of experience, Dune crest has established itself as a pioneer supplier of new, used and reconditioned earthmoving equipment. Our dedicated team is always on-hand to assist you and advise on the most suitable equipment for your earthmoving project.</p>
  <p class="about-text abs" style="top:1670px">Our goal is to provide high-quality products and ensure your machine runs effectively. Get in touch today!</p>
  <a class="btn" href="#">About Us</a>
  <div class="about-photo abs" role="img" aria-label="Two site workers in hard hats and safety vests beside an excavator at a quarry"></div>
</section>

<h2 class="section-title abs" style="top:1943px">Select Industry</h2>

<div class="industry-strip abs">
  <div class="industry-tile" role="img" aria-label="Rock breaker working on a construction site" style="background:linear-gradient(160deg,#8a7a6a,#5a4230)"><div class="name" style="top:106px">Construction</div></div>
  <div class="industry-tile" role="img" aria-label="Golden wheat field" style="background:linear-gradient(160deg,#d59a2a,#a86c14)"><div class="name" style="top:106px">Rural</div></div>
  <div class="industry-tile" role="img" aria-label="Gravel stockpiles" style="background:linear-gradient(160deg,#8c8a86,#5c5a56)">
    <div class="name" style="top:92px">Material<br>Handling Solution</div>
    <svg class="arrow-icon" style="left:105px;top:169px" width="30" height="30" viewBox="0 0 30 30"><circle cx="15" cy="15" r="13" fill="none" stroke="#f8b12e" stroke-width="2"/><path d="M9 15h11M16 10l5 5-5 5" fill="none" stroke="#f8b12e" stroke-width="2"/></svg>
  </div>
  <div class="industry-tile" role="img" aria-label="Underground mine tunnel" style="background:linear-gradient(160deg,#6a4a30,#2e2018)"><div class="name" style="top:106px">Mining</div></div>
  <div class="industry-tile" role="img" aria-label="Railway tracks through green fields" style="background:linear-gradient(180deg,#7fa060,#7a6f62 40%,#4a4640)"><div class="name" style="top:106px">Railways</div></div>
</div>

<div class="cta-bar abs">
  <div class="item" style="left:154px">
    <svg width="32" height="32" viewBox="0 0 32 32"><circle cx="16" cy="16" r="16" fill="#1d1d1d"/><path d="M10 22l1-4 8-8 3 3-8 8z" fill="#f8b12e"/></svg>
    Request a price
  </div>
  <div class="divider" style="left:417px"></div>
  <div class="item" style="left:530px">
    <svg width="32" height="32" viewBox="0 0 32 32"><circle cx="16" cy="16" r="16" fill="#1d1d1d"/><path d="M10 22l1-4 8-8 3 3-8 8z" fill="#f8b12e"/></svg>
    Get in touch
  </div>
  <div class="divider" style="left:786px"></div>
  <div class="item" style="left:883px">
    <svg width="32" height="32" viewBox="0 0 32 32"><circle cx="16" cy="16" r="16" fill="#1d1d1d"/><path d="M11 9c.7-.7 1.5-.7 2 0l1.5 2.2c.4.7 0 1.4-.7 1.8-.4.4 0 1.1.7 2.2s1.8 1.8 2.2 1.5c.4-.7 1.1-1.1 1.8-.7l2.2 1.5c.7.7.7 1.5 0 2.2-1.5 1.5-3.7.7-6.6-2.2S9.5 11.5 11 9z" fill="#f8b12e"/></svg>
    Call: 0491 570 156
  </div>
</div>

<section class="testimonial abs" role="img" aria-label="Dark, faded excavator silhouette on a work site">
  <blockquote>“ Lorem ipsum dolor sit amet, consectetur adipiscing elit, sed do eiusmod tempor incididunt ut labore et dolore magna aliqua...</blockquote>
  <cite>- DANA MARSH -</cite>
</section>

<div class="social-bar abs" aria-label="Social links">
  <span class="dot" style="left:478px"></span>
  <span class="dot" style="left:535px"></span>
  <span class="dot" style="left:592px"></span>
  <span class="dot" style="left:649px"></span>
  <span class="dot" style="left:706px"></span>
</div>

<footer class="site-footer abs">
  <p class="copyright abs">© 2018 Dune <span>crest</span></p>
  <nav class="footer-nav label">
    <a class="current" href="#" style="left:407px">Company</a>
    <a href="#" style="left:487px">Equipment</a>
    <a href="#" style="left:580px">Industry</a>
    <a href="#" style="left:664px">Services</a>
    <a href="#" style="left:744px">Contact</a>
  </nav>
  <div class="back-top abs label">Back to top
    <svg width="12" height="8" viewBox="0 0 12 8"><path d="M1 7l5-5 5 5" fill="none" stroke="#ddd" stroke-width="1.5"/></svg>
  </div>
</footer>

</body>
</html>
```